Elegant and modern body scrub for organic junkies

I need a package design for my new company based out of Austin, Texas. We are focused on cruelty free and all natural and organic products. Our deign needs to be able to have the information we require on it, while still appearing very clean and captivating. Our initial product is a clear skin body scrub, intended for people with problematic skin. Our target market is women and we want to show elegance, without appearing "high end."
Updates

Reason: I want to allot more time for certain designers to submit edits. Last minute proposals have been appealing

Target Market(s)

Women. Organic and holistic minded. Natural beauty lovers.

Industry/Entity Type

Skin Care Product

Font styles to use
Script
Other font styles liked:
• AmericanTypewriter, Beautifulflaws, courier, caviarDreams-bold

Colors
000000
ffc214
ffffff
fece3e
fbee3e

Requirements
Must have
• Must be designed in Adobe Illustrator.
• The photo titled “structure for oz and grams” -That needs to be included at the bottom of 1B. I like the horizontal and vertical bar that separate the two. I want that.
• Color Inspiration - The photo titled “venra color inspiration” and “color combo inspiration” are the colors I want. BLACK, GOLD, WHITE. I want the label background black and the writing in white with some gold somewhere on it. My logo is going to be a golden elephant.
• The photos titled “I like how clean this looks” and “I also like how clean this looks” - I want 1B to look super clean. I don’t want a lot of information in this box. I want simple and clean. This is where the logo and brand name will go.
• Logo - A golden elephant. I want it to be gold and geometric. There can be dimension like this elephant example on the left of the 1B description. I want the trunk to be facing to the left and the trunk needs to be raised overhead and touching the animal's forehead.
• The photo titled “sideways writing and silver rim” - I want 1C to be written sideways like this. My text will be much more extensive so the font won’t be able to be so big.
Nice to have
• The photo titled “sideways writing and silver rim” - I want 1C to be written sideways like this. My text will be much more extensive so the font won’t be able to be so big. I also REALLY like how this label is rimmed in silver, but I would want gold. This is not mandatory, but I really like this.
• The photo titled “melted honey” - This is another option I really like. The gold that looks like honey dripping on the label is really cool. Not mandatory, but I really liked that. I also like the craft background on this.
• Color Inspiration - The photo titled “color inspiration” and “another color inspiration” is an option I would also like to see. Rather than black, I’d like to see what it would ALSO look like with a navy background. NAVY, GOLD, WHITE, maybe black somewhere.
Should not have
• Colorful patterns or excessive info in section 1B.

```html
<!DOCTYPE html>
<html lang="en">
<head>
<meta charset="UTF-8">
<title>Clear Skin Body Polish Label</title>
<link rel="stylesheet" href="https://fonts.googleapis.com/css2?family=Josefin+Sans:wght@300;400;600&display=swap">
<style>
  :root {
    --page-bg: #ededed;
    --label-black: #000000;
    --panel-black: #141414;
    --gold-deep: #a8791a;
    --gold-mid: #d9a62c;
    --gold-light: #f5cf5a;
    --band-gold: #b8923a;
    --text-white: #ffffff;
  }
  * { margin: 0; padding: 0; box-sizing: border-box; }
  html, body {
    width: 1200px;
    height: 1200px;
    overflow: hidden;
    background: var(--page-bg);
  }
  .label {
    position: absolute;
    left: 100px;
    top: 200px;
    width: 1000px;
    height: 800px;
    background: var(--label-black);
    overflow: hidden;
  }
  .gold-band {
    position: absolute;
    left: 0;
    top: 275px;
    width: 100%;
    height: 245px;
    background: linear-gradient(90deg, var(--gold-deep), var(--band-gold) 30%, var(--gold-mid) 70%, var(--gold-deep));
  }
  .medallion {
    position: absolute;
    left: 145px;
    top: 45px;
    width: 710px;
    height: 710px;
  }
  .brand-mark {
    position: absolute;
    left: 0;
    width: 100%;
    top: 250px;
    text-align: center;
    font-family: 'Josefin Sans', sans-serif;
    font-weight: 600;
    font-size: 52px;
    letter-spacing: 4px;
    color: var(--gold-light);
  }
  .brand-name {
    position: absolute;
    left: 0;
    width: 100%;
    top: 400px;
    text-align: center;
    font-family: 'Josefin Sans', sans-serif;
    font-weight: 600;
    font-size: 70px;
    letter-spacing: 2px;
    color: var(--gold-light);
  }
  .product-name {
    position: absolute;
    left: 0;
    width: 100%;
    top: 500px;
    text-align: center;
    font-family: 'Josefin Sans', sans-serif;
    font-weight: 300;
    font-size: 44px;
    line-height: 50px;
    letter-spacing: 1px;
    color: var(--text-white);
  }
  .net-weight {
    position: absolute;
    right: 92px;
    top: 722px;
    font-family: 'Josefin Sans', sans-serif;
    font-weight: 400;
    font-size: 22px;
    letter-spacing: 1px;
    color: var(--text-white);
  }
  .net-weight .divider { margin: 0 10px; }
</style>
</head>
<body>
  <main class="label">
    <div class="gold-band"></div>

    <svg class="medallion" viewBox="0 0 710 710">
      <defs>
        <radialGradient id="ornament-gold" cx="50%" cy="50%" r="50%">
          <stop offset="78%" stop-color="#c8952a"/>
          <stop offset="90%" stop-color="#e9b945"/>
          <stop offset="100%" stop-color="#b07f1f"/>
        </radialGradient>
        <linearGradient id="rim-gold" x1="0" y1="0" x2="1" y2="1">
          <stop offset="0%" stop-color="#f5cf5a"/>
          <stop offset="100%" stop-color="#b8861f"/>
        </linearGradient>
      </defs>
      <path class="ornament-ring" role="img" aria-label="Ornate gold filigree mandala border encircling the emblem"
            fill="url(#ornament-gold)" fill-rule="evenodd"
            d="M355 0 A355 355 0 1 1 354.9 0 Z M355 62 A293 293 0 1 0 355.1 62 Z"/>
      <circle class="emblem-panel" cx="355" cy="355" r="293" fill="var(--panel-black)"/>
      <circle class="emblem-rim" cx="355" cy="355" r="283" fill="none" stroke="url(#rim-gold)" stroke-width="5"/>
    </svg>

    <div class="brand-mark">venra</div>
    <h1 class="brand-name">BRAND NAME</h1>
    <p class="product-name">Clear Skin<br>Body Polish</p>
    <p class="net-weight">12 oz<span class="divider">|</span>340g</p>
  </main>
</body>
</html>
```